Lanterne architecture business cards

We are a new company based in New Zealand. We Specialize in High end Luxury Residential Architecture.

Every home is bespoke and is designed to each clients individual requirements and needs.

I like to design buildings that inspire people through light and form while offering a high level of comfort and usability.

Lines of sight, proportion and balance are fundamental to the spaces I create.
Updates

August 5th is current deadline - Today's date is the 13th of August.

Target Market(s)

New Zealanders who want a custom individual home design, typically 30-65 year old males and females

Industry/Entity Type

Architecture

Contact Information for Business Card

Director - Derek Tolson
Contact Number - 0279164073
Email - info@lanternearchitecture-example.co.nz
Webstie - www.lanternearchitecture-example.co.nz
Social Media - @lanternearchitecture

Font styles to use
Sans Serif

Requirements
Must have
• Logo (Both Sides)
Website
Email
Contact Number
Social Media

Nice to have
• Texture
Should not have
• More than 3 colours - typically I would've thought 2 would be good to match the logo.

```html
<!DOCTYPE html>
<html lang="en">
<head>
<meta charset="utf-8">
<title>Lanterne Architecture – Business Cards</title>
<link href="https://fonts.googleapis.com/css2?family=Josefin+Sans:wght@300&family=Roboto:wght@400;500&display=swap" rel="stylesheet">
<style>
  :root {
    --backdrop: #6f6f6f;
    --card: #262626;
    --card-edge: #1e1e1e;
    --wordmark: #c9c9c9;
    --name: #cfcfcf;
    --text: #e8e8e8;
    --rule: #8a8a8a;
  }
  html, body {
    margin: 0;
    padding: 0;
    width: 1200px;
    height: 960px;
    overflow: hidden;
    background: var(--backdrop);
  }
  .canvas {
    position: relative;
    width: 1200px;
    height: 960px;
  }
  .card {
    position: absolute;
    background: var(--card);
    box-shadow: 0 2px 6px rgba(0,0,0,0.45);
    border: 1px solid var(--card-edge);
    box-sizing: border-box;
  }
  .card-front {
    left: 76px;
    top: 167px;
    width: 360px;
    height: 630px;
  }
  .card-back {
    left: 490px;
    top: 430px;
    width: 630px;
    height: 362px;
  }
  .wordmark {
    position: absolute;
    text-align: center;
    font-family: "Josefin Sans", sans-serif;
    font-weight: 300;
    color: var(--wordmark);
    text-transform: uppercase;
    margin: 0;
  }
  .wordmark .primary { display: block; }
  .wordmark .secondary { display: block; }

  .card-front .wordmark {
    left: 0;
    width: 100%;
    top: 542px;
  }
  .card-front .wordmark .primary {
    font-size: 27px;
    letter-spacing: 12px;
    padding-left: 12px;
    line-height: 30px;
  }
  .card-front .wordmark .secondary {
    font-size: 9px;
    letter-spacing: 14.5px;
    padding-left: 14px;
    line-height: 14px;
    margin-top: 4px;
  }

  .brand-dot {
    position: absolute;
    left: 135px;
    top: 122px;
    width: 42px;
    height: 42px;
    border: 6px solid var(--text);
    border-radius: 50%;
    box-sizing: border-box;
  }
  .card-back .wordmark {
    left: 30px;
    width: 260px;
    top: 200px;
  }
  .card-back .wordmark .primary {
    font-size: 24px;
    letter-spacing: 11px;
    padding-left: 11px;
    line-height: 26px;
  }
  .card-back .wordmark .secondary {
    font-size: 8px;
    letter-spacing: 12.5px;
    padding-left: 12px;
    line-height: 12px;
    margin-top: 3px;
  }

  .divider {
    position: absolute;
    left: 306px;
    top: 118px;
    width: 1px;
    height: 126px;
    background: var(--rule);
  }
  .contact {
    position: absolute;
    left: 322px;
    top: 112px;
    font-family: "Roboto", sans-serif;
  }
  .contact-name {
    margin: 0 0 10px;
    font-size: 21px;
    font-weight: 500;
    color: var(--name);
    letter-spacing: 0.3px;
    text-transform: uppercase;
  }
  .contact-list {
    list-style: none;
    margin: 0;
    padding: 0;
  }
  .contact-list li {
    display: flex;
    align-items: center;
    font-size: 14.5px;
    color: var(--text);
    line-height: 23px;
  }
  .contact-icon {
    width: 12px;
    height: 12px;
    margin-right: 6px;
    flex: none;
    fill: var(--text);
  }
  .social-dot {
    width: 9px;
    height: 9px;
    margin: 0 8px 0 2px;
    border: 1.5px solid var(--text);
    border-radius: 50%;
    box-sizing: border-box;
    flex: none;
  }
</style>
</head>
<body>
<main class="canvas">

  <section class="card card-front" aria-label="Card front">
    <h1 class="wordmark">
      <span class="primary">Lanterne</span>
      <span class="secondary">Architecture</span>
    </h1>
  </section>

  <section class="card card-back" aria-label="Card back">
    <span class="brand-dot" aria-hidden="true"></span>
    <h2 class="wordmark">
      <span class="primary">Lanterne</span>
      <span class="secondary">Architecture</span>
    </h2>

    <div class="divider"></div>

    <div class="contact">
      <p class="contact-name">Derek Tolson</p>
      <ul class="contact-list">
        <li>
          <svg class="contact-icon" viewBox="0 0 24 24" aria-hidden="true"><path d="M6.6 10.8a15.1 15.1 0 0 0 6.6 6.6l2.2-2.2a1 1 0 0 1 1-.25 11.4 11.4 0 0 0 3.6.57 1 1 0 0 1 1 1V20a1 1 0 0 1-1 1A17 17 0 0 1 3 4a1 1 0 0 1 1-1h3.5a1 1 0 0 1 1 1c0 1.25.2 2.45.57 3.57a1 1 0 0 1-.25 1z"/></svg>
          0279164073
        </li>
        <li>
          <svg class="contact-icon" viewBox="0 0 24 24" aria-hidden="true"><path d="M2 5h20v14H2z M3.5 6.5 12 12.5l8.5-6" fill="none" stroke="#e8e8e8" stroke-width="0"/><path d="M2 5h20v2l-10 6.5L2 7z"/><path d="M2 9l10 6.5L22 9v10H2z"/></svg>
          info@lanternearchitecture-example.co.nz
        </li>
        <li>
          <svg class="contact-icon" viewBox="0 0 24 24" aria-hidden="true"><circle cx="12" cy="12" r="10" fill="none" stroke="#e8e8e8" stroke-width="2.5"/><path d="M2 12h20M12 2c3 3 3 17 0 20M12 2c-3 3-3 17 0 20" fill="none" stroke="#e8e8e8" stroke-width="2"/></svg>
          www.lanternearchitecture-example.co.nz
        </li>
        <li>
          <span class="social-dot" aria-hidden="true"></span>
          @lanternearchitecture
        </li>
      </ul>
    </div>
  </section>

</main>
</body>
</html>
```